we are in the infrastructure business ( road construction ) and I need a billboard that I placed it at every project to illustrate that we worked there . We have the logo , I attached it , I just need an interesting design of the billboard.
The company s name is : Vextra Civil - I attached how to be written !
I don't need to write road construction business on it

Requirements
Must have
• Study the design of the logo I attached ( the sign with " KTP " is just an example !!
Nice to have
• the romanian flag but made into a special form ( I attached an Idea )

```html
<!DOCTYPE html>
<html lang="en">
<head>
<meta charset="UTF-8">
<title>Vextra Civil Billboard</title>
<link href="https://fonts.googleapis.com/css2?family=Montserrat:wght@600;700;800&display=swap" rel="stylesheet">
<style>
  :root {
    --stage: #1b2236;
    --board-blue: #2f5fa5;
    --board-blue-dark: #254f8e;
    --brand-yellow: #f7c417;
    --white: #ffffff;
    --hazard-dark: #1f3f75;
  }
  * { box-sizing: border-box; margin: 0; padding: 0; }
  html, body {
    width: 1200px; height: 792px; overflow: hidden;
    background: var(--stage);
    font-family: "Montserrat", sans-serif;
  }
  .billboard {
    position: absolute; left: 30px; top: 113px;
    width: 1140px; height: 566px;
    background: linear-gradient(180deg, var(--board-blue) 0%, var(--board-blue-dark) 100%);
    overflow: hidden;
  }
  .photo {
    position: absolute; top: 65px; height: 453px;
  }
  .photo--site {
    left: 54px; width: 280px;
    background: linear-gradient(180deg, #7a6a63 0%, #d9a066 30%, #b7865e 52%, #6d6f74 70%, #4e5258 100%);
  }
  .photo--roller {
    left: 807px; width: 282px;
    background: linear-gradient(180deg, #f2efe9 0%, #e7d3b0 35%, #c98a45 55%, #3a3a3c 75%, #1f1f21 100%);
  }
  .brand-mark {
    position: absolute; left: 0; width: 100%; top: 92px;
    text-align: center;
    color: var(--white);
    font-weight: 700; font-size: 34px; letter-spacing: 6px;
  }
  .headline {
    position: absolute; left: 334px; width: 473px; top: 160px;
    text-align: center; font-weight: 800; line-height: 0.98;
    font-size: 96px;
  }
  .headline__top { display: block; color: var(--brand-yellow); }
  .headline__bottom { display: block; color: var(--white); }
  .cta {
    position: absolute; left: 389px; top: 369px; width: 360px; height: 74px;
    border: 2px solid var(--white); border-radius: 8px;
    display: flex; align-items: center; gap: 12px; padding: 0 16px;
  }
  .cta__icon { width: 40px; height: 40px; flex: none; }
  .cta__label { color: var(--white); font-weight: 700; font-size: 15px; letter-spacing: 0.3px; }
  .cta__phone { color: var(--brand-yellow); font-weight: 800; font-size: 32px; line-height: 1.05; }
  .decor { position: absolute; }
</style>
</head>
<body>
  <main class="billboard">
    <div class="photo photo--site" role="img" aria-label="Road engineer in high-visibility workwear holding a tablet on a new road at sunset, with a loader behind"></div>
    <div class="photo photo--roller" role="img" aria-label="Orange road roller compacting fresh asphalt"></div>

    <svg class="decor" style="left:0;top:0" width="1140" height="566" viewBox="0 0 1140 566" aria-hidden="true">
      <!-- hazard stripes -->
      <g fill="var(--brand-yellow)">
        <polygon points="1117,8 1134,-4 1134,14 1117,26"/>
        <polygon points="1117,38 1134,26 1134,44 1117,56"/>
        <polygon points="1117,68 1134,56 1134,74 1117,86"/>
        <polygon points="1117,98 1134,86 1134,104 1117,116"/>
        <polygon points="3,460 20,448 20,466 3,478"/>
        <polygon points="3,490 20,478 20,496 3,508"/>
        <polygon points="3,520 20,508 20,526 3,538"/>
        <polygon points="3,550 20,538 20,556 3,568"/>
      </g>
      <!-- triangles -->
      <g fill="var(--white)">
        <polygon points="352,30 358,22 364,30"/>
        <polygon points="352,46 358,38 364,46"/>
        <polygon points="352,62 358,54 364,62"/>
        <polygon points="352,78 358,70 364,78"/>
        <polygon points="776,486 782,494 788,486"/>
        <polygon points="776,502 782,510 788,502"/>
        <polygon points="776,518 782,526 788,518"/>
        <polygon points="776,534 782,542 788,534"/>
      </g>
      <!-- circles -->
      <g fill="none" stroke="var(--white)" stroke-width="2" opacity="0.85">
        <circle cx="750" cy="68" r="38"/>
        <circle cx="750" cy="68" r="30"/>
        <circle cx="390" cy="506" r="42"/>
        <circle cx="390" cy="506" r="34"/>
      </g>
      <circle cx="690" cy="82" r="5" fill="none" stroke="var(--white)" stroke-width="2"/>
      <!-- dot columns -->
      <g fill="var(--white)" opacity="0.8">
        <circle cx="40" cy="110" r="2"/><circle cx="40" cy="122" r="2"/><circle cx="40" cy="134" r="2"/><circle cx="40" cy="146" r="2"/><circle cx="40" cy="158" r="2"/>
        <circle cx="1104" cy="436" r="2"/><circle cx="1104" cy="448" r="2"/><circle cx="1104" cy="460" r="2"/><circle cx="1104" cy="472" r="2"/><circle cx="1104" cy="484" r="2"/>
      </g>
    </svg>

    <div class="brand-mark">VEXTRA CIVIL</div>

    <h1 class="headline">
      <span class="headline__top">VEXTRA</span>
      <span class="headline__bottom">CIVIL</span>
    </h1>

    <div class="cta">
      <svg class="cta__icon" viewBox="0 0 40 40" aria-hidden="true">
        <path d="M10 6 l6 0 l3 8 l-4 3 c2 4 5 7 9 9 l3 -4 l8 3 l0 6 c0 2 -2 4 -4 4 c-14 -1 -24 -11 -25 -25 c0 -2 2 -4 4 -4 z" fill="var(--brand-yellow)"/>
        <path d="M24 6 a10 10 0 0 1 10 10" fill="none" stroke="var(--brand-yellow)" stroke-width="2.5" stroke-linecap="round"/>
        <path d="M24 12 a4 4 0 0 1 4 4" fill="none" stroke="var(--brand-yellow)" stroke-width="2.5" stroke-linecap="round"/>
      </svg>
      <div>
        <div class="cta__label">CALL TO FIND OUT MORE</div>
        <div class="cta__phone">+012 555 0147</div>
      </div>
    </div>
  </main>
</body>
</html>
```